Business Card and Stationary Design

After the successful redesign of our logo we are wanting to follow suite and create a new business card and stationary design!

New Logo is attached, information required on the business card should contain a mixture of the following but layout/arrangement is up to the designer.

Happy if the national provider number and abn are on the back, and happy for them to be smaller than the rest.

I am also happy to receive single sided or weird and wonderful designs.

Name
Title
National Provider Number 7291
ABN 53 219 864 317
Level 3, 42 Marlow Street
Kelby Heights NSW 2291
Ph: 1300 987 214
Mobile: 0432 785 619
name@ferngatebuild.com.au
www.ferngatebuild.com.au

Target Market(s)

Professionals, Peers, Students, Suppliers...

Industry/Entity Type

Construction

Contact Information for Business Card

Listed in project description

Font styles to use
Other font styles liked:
• Century Gothic

Colors
0455a3
3176b5
ffffff

Requirements
Must have
• Professional Design, same color scheme as our logo
Nice to have
• Something that sets our apart from everyone else would be fantastic, open to size and shape and layout options, as long as they present professionally.
• Open to raised/embossed text, alternative materials, custom sizes, clear material
Should not have
• The color orange

```html
<!DOCTYPE html>
<html lang="en">
<head>
<meta charset="utf-8">
<title>Ferngate Build — Letterhead</title>
<link rel="stylesheet" href="https://fonts.googleapis.com/css2?family=Didact+Gothic&display=swap">
<style>
  :root {
    --backdrop: #8e8b9b;
    --paper: #ffffff;
    --brand-blue: #2e4a9a;
    --brand-blue-light: #3176b5;
    --ink-grey: #8a8a8a;
    --rule-grey: #b5b5b5;
  }
  * { margin: 0; padding: 0; box-sizing: border-box; }
  html, body { width: 1200px; height: 1200px; overflow: hidden; }
  body {
    background: var(--backdrop);
    font-family: "Didact Gothic", "Century Gothic", sans-serif;
    display: flex; align-items: center; justify-content: center;
  }
  .letterhead {
    position: relative;
    width: 778px; height: 1100px;
    background: var(--paper);
    box-shadow: 0 6px 24px rgba(40, 36, 60, 0.25);
  }
  .brand {
    position: absolute; left: 64px; top: 150px;
    display: flex; align-items: center; gap: 12px;
  }
  .brand-square { width: 30px; height: 30px; background: var(--brand-blue); }
  .brand-name { font-size: 40px; color: var(--brand-blue); letter-spacing: 0.5px; line-height: 1; }
  .contact {
    position: absolute; right: 56px; top: 52px;
    list-style: none; text-align: right;
    font-size: 14px; line-height: 20px;
  }
  .contact li { display: flex; justify-content: flex-end; align-items: center; gap: 8px; }
  .contact .grey { color: var(--ink-grey); }
  .contact .blue { color: var(--brand-blue); }
  .contact svg { width: 12px; height: 12px; flex: none; }
  .accent-dashes { position: absolute; display: flex; gap: 5px; }
  .accent-dashes span { width: 36px; height: 1.5px; background: var(--brand-blue-light); }
  .accent-dashes.header { right: 56px; top: 150px; }
  .accent-dashes.footer { right: 56px; top: 968px; }
  .rule { position: absolute; height: 1px; background: var(--rule-grey); }
  .rule.header { left: 64px; right: 56px; top: 218px; }
  .rule.footer { left: 64px; right: 56px; top: 1010px; }
  .registration {
    position: absolute; right: 56px; top: 982px;
    font-size: 12px; color: var(--ink-grey); white-space: nowrap;
  }
  .registration .num { color: var(--brand-blue); }
  .address {
    position: absolute; left: 64px; top: 1024px;
    font-size: 13px; color: var(--brand-blue); white-space: nowrap;
  }
</style>
</head>
<body>
  <main class="letterhead">
    <header>
      <div class="brand">
        <span class="brand-square"></span>
        <span class="brand-name">ferngate build</span>
      </div>
      <ul class="contact">
        <li><span class="grey">1300 987 214</span>
          <svg viewBox="0 0 12 12"><path d="M2 2h3l1 3-1.5 1a6 6 0 0 0 2 2L8 6.5l3 1V10a1 1 0 0 1-1 1A9 9 0 0 1 1 3a1 1 0 0 1 1-1z" fill="var(--ink-grey)"/></svg></li>
        <li><span class="grey">0432 785 619</span>
          <svg viewBox="0 0 12 12"><rect x="3" y="1" width="6" height="10" rx="1" fill="none" stroke="var(--ink-grey)"/><circle cx="6" cy="9.2" r=".7" fill="var(--ink-grey)"/></svg></li>
        <li><span class="blue">name@ferngatebuild.com.au</span>
          <svg viewBox="0 0 12 12"><rect x="1" y="2.5" width="10" height="7" fill="none" stroke="var(--ink-grey)"/><path d="M1 2.5l5 4 5-4" fill="none" stroke="var(--ink-grey)"/></svg></li>
        <li><span class="blue">www.ferngatebuild.com.au</span>
          <svg viewBox="0 0 12 12"><circle cx="6" cy="6" r="5" fill="none" stroke="var(--ink-grey)"/><ellipse cx="6" cy="6" rx="2.2" ry="5" fill="none" stroke="var(--ink-grey)"/><path d="M1 6h10" stroke="var(--ink-grey)"/></svg></li>
      </ul>
      <div class="accent-dashes header"><span></span><span></span><span></span><span></span></div>
      <div class="rule header"></div>
    </header>
    <footer>
      <div class="accent-dashes footer"><span></span><span></span><span></span><span></span></div>
      <p class="registration">National Provider Number <span class="num">7291</span> • ABN <span class="num">53 219 864 317</span></p>
      <div class="rule footer"></div>
      <p class="address">Level 3, 42 Marlow Street, Kelby Heights NSW 2291</p>
    </footer>
  </main>
</body>
</html>
```